Equity, Effectiveness and Efficiency in charitable food relief sector

I am undertaking my PhD in food policy in the charitable food relief sector, specifically investigating the factors (supply, demand and capacity) that affect the introduction of nutrition policy and in turn, affect the sector's ability to achieve equity, effectiveness and efficiency.

I need a graphic device that incorporates this central idea of Equity, Effectiveness and Efficiency, and how the factors of supply, demand and capacity interact. There are sub-factors within supply (1-6), demand (7-10) and capacity (11 - 15). All these details are shown in the attached figure (Basic figure_Eq Effec Effic and factors.jpg)

This figure (Basic figure_Eq Effec Effic and factors.jpg) contains all the information I need in a graphic but I need something that is more visually appealing, and that can link the ideas in a format other than a table. The final graphic will outline how the food relief sector balances the core objectives of equity, effectiveness and efficiency with the factors (and sub-factors) of supply, demand and capacity.

```html
<!DOCTYPE html>
<html lang="en">
<head>
<meta charset="utf-8">
<title>Equity, Effectiveness and Efficiency in Charitable Food Relief</title>
<link rel="stylesheet" href="https://fonts.googleapis.com/css2?family=Kanit:wght@400;600&family=Roboto+Condensed:wght@700&display=swap">
<style>
  :root {
    --supply-bar: #3d566e;
    --supply-ring: #4a90c8;
    --demand-bar: #c94b56;
    --demand-ring: #be1e2d;
    --capacity-bar: #bfb540;
    --capacity-ring: #f5e834;
    --detail-box: #d5d28a;
    --detail-pointer: #cac66c;
    --detail-text: #6f6a1c;
    --policy-ring: #f9ad40;
    --core: #66ccf2;
    --white: #ffffff;
    --ink: #111111;
  }
  html, body {
    margin: 0;
    padding: 0;
    width: 1200px;
    height: 849px;
    overflow: hidden;
    background: var(--white);
  }
  .framework {
    display: block;
    width: 1200px;
    height: 849px;
  }
  .factor-label {
    font-family: "Kanit", sans-serif;
    font-weight: 600;
    font-size: 17px;
    fill: var(--white);
  }
  .factor-label--right { text-anchor: end; }
  .detail-list {
    font-family: "Kanit", sans-serif;
    font-weight: 400;
    font-size: 16px;
    fill: var(--detail-text);
  }
  .ring-title {
    font-family: "Kanit", sans-serif;
    font-weight: 600;
    font-size: 33px;
    letter-spacing: 9px;
  }
  .ring-title--supply { fill: var(--white); }
  .ring-title--demand { fill: var(--white); }
  .ring-title--capacity { fill: var(--ink); }
  .policy-caption {
    font-family: "Kanit", sans-serif;
    font-weight: 400;
    font-size: 24px;
    fill: var(--ink);
  }
  .core-objective {
    font-family: "Roboto Condensed", sans-serif;
    font-weight: 700;
    font-size: 34px;
    fill: var(--white);
    text-anchor: middle;
  }
</style>
</head>
<body>
<svg class="framework" viewBox="0 0 1200 849" xmlns="http://www.w3.org/2000/svg" aria-label="Factors of supply, demand and capacity affecting equity, effectiveness and efficiency in charitable food relief">
  <defs>
    <radialGradient id="halo" cx="521" cy="417" r="340" gradientUnits="userSpaceOnUse">
      <stop offset="0.78" stop-color="#000" stop-opacity="0.7"/>
      <stop offset="0.9" stop-color="#000" stop-opacity="0.25"/>
      <stop offset="1" stop-color="#000" stop-opacity="0"/>
    </radialGradient>
    <path id="arc-demand" d="M590.5,203 A225 225 0 0 1 746,417"/>
    <path id="arc-capacity" d="M564.4,663.2 A250 250 0 0 0 767.2,460.4"/>
    <path id="arc-supply" d="M314.3,472.4 A214 214 0 0 1 383.4,253.1"/>
    <path id="arc-policy" d="M363.1,474.5 A168 168 0 1 1 678.9,474.5"/>
  </defs>

  <!-- Supply factor bars -->
  <g class="supply-factors">
    <rect x="84" y="136" width="520" height="88" fill="var(--supply-bar)"/>
    <rect x="84" y="229" width="520" height="89" fill="var(--supply-bar)"/>
    <rect x="84" y="323" width="520" height="88" fill="var(--supply-bar)"/>
    <rect x="84" y="416" width="520" height="88" fill="var(--supply-bar)"/>
    <rect x="84" y="509" width="520" height="89" fill="var(--supply-bar)"/>
    <rect x="84" y="603" width="520" height="88" fill="var(--supply-bar)"/>
  </g>

  <!-- Demand factor bars -->
  <g class="demand-factors">
    <rect x="520" y="136" width="438" height="57" fill="var(--demand-bar)"/>
    <rect x="520" y="199" width="438" height="59" fill="var(--demand-bar)"/>
    <rect x="520" y="263" width="438" height="59" fill="var(--demand-bar)"/>
    <rect x="520" y="327" width="438" height="60" fill="var(--demand-bar)"/>
  </g>

  <!-- Capacity factor bars -->
  <g class="capacity-factors">
    <rect x="520" y="392" width="438" height="55" fill="var(--capacity-bar)"/>
    <rect x="520" y="452" width="438" height="56" fill="var(--capacity-bar)"/>
    <rect x="520" y="513" width="438" height="55" fill="var(--capacity-bar)"/>
    <rect x="520" y="574" width="438" height="55" fill="var(--capacity-bar)"/>
    <rect x="520" y="634" width="438" height="57" fill="var(--capacity-bar)"/>
  </g>

  <!-- Capacity detail callouts -->
  <g class="capacity-details">
    <polygon points="958,392 975,382 975,457 958,447" fill="var(--detail-pointer)"/>
    <rect x="975" y="382" width="139" height="75" fill="var(--detail-box)"/>
    <polygon points="958,508 975,480 975,646 958,574" fill="var(--detail-pointer)"/>
    <rect x="975" y="480" width="139" height="166" fill="var(--detail-box)"/>
  </g>

  <!-- Shadow halo around wheel -->
  <circle cx="521" cy="417" r="340" fill="url(#halo)"/>

  <!-- Wheel -->
  <g class="wheel">
    <circle cx="521" cy="417" r="281" fill="var(--white)"/>
    <path class="segment-demand" d="M521,140 A277 277 0 0 1 796.5,445.9 L726.9,438.6 A207 207 0 0 0 521,210 Z" fill="var(--demand-ring)" stroke="var(--white)" stroke-width="3"/>
    <path class="segment-capacity" d="M796.5,445.9 A277 277 0 0 1 463.4,687.9 L478,619.5 A207 207 0 0 0 726.9,438.6 Z" fill="var(--capacity-ring)" stroke="var(--white)" stroke-width="3"/>
    <path class="segment-supply" d="M463.4,687.9 A277 277 0 0 1 521,140 L521,210 A207 207 0 0 0 478,619.5 Z" fill="var(--supply-ring)" stroke="var(--white)" stroke-width="3"/>
    <circle cx="521" cy="417" r="197" fill="var(--policy-ring)"/>
    <circle cx="521" cy="417" r="144" fill="var(--core)"/>
  </g>

  <!-- Ring titles -->
  <text class="ring-title ring-title--supply"><textPath href="#arc-supply" startOffset="24">SUPPLY</textPath></text>
  <text class="ring-title ring-title--demand"><textPath href="#arc-demand" startOffset="10">DEMAND</textPath></text>
  <text class="ring-title ring-title--capacity"><textPath href="#arc-capacity" startOffset="32">CAPACITY</textPath></text>

  <!-- Policy caption -->
  <text class="policy-caption"><textPath href="#arc-policy" startOffset="4" textLength="630" lengthAdjust="spacing">Factors affecting the introduction of nutrition policy</textPath></text>

  <!-- Core objectives -->
  <g class="core-objectives">
    <text class="core-objective" x="521" y="391">EQUITY</text>
    <text class="core-objective" x="521" y="428" textLength="222" lengthAdjust="spacingAndGlyphs">EFFECTIVENESS</text>
    <text class="core-objective" x="521" y="465">EFFICIENCY</text>
  </g>

  <!-- Supply labels -->
  <g class="factor-label">
    <text x="103" y="164">Uncertain</text>
    <text x="103" y="185">Material</text>
    <text x="103" y="206">Supply</text>
    <text x="103" y="258">Uncertain</text>
    <text x="103" y="279">Monetary</text>
    <text x="103" y="300">Supply</text>
    <text x="103" y="352">Limited</text>
    <text x="103" y="373">Food</text>
    <text x="103" y="394">Supply</text>
    <text x="103" y="465">Perishability</text>
    <text x="103" y="554">Donor</text>
    <text x="103" y="575">Constraints</text>
    <text x="103" y="641">Donor</text>
    <text x="103" y="662">Relationships</text>
  </g>

  <!-- Demand and capacity labels -->
  <g class="factor-label factor-label--right">
    <text x="939" y="161">Uncertain</text>
    <text x="939" y="182">Demand</text>
    <text x="939" y="224">Limited</text>
    <text x="939" y="245">Demand Visibility</text>
    <text x="939" y="289">Client</text>
    <text x="939" y="310">Choice</text>
    <text x="939" y="352">Food</text>
    <text x="939" y="373">Wastage</text>
    <text x="939" y="425">Storage</text>
    <text x="939" y="486">Transportation</text>
    <text x="939" y="547">Workforce</text>
    <text x="939" y="598">External</text>
    <text x="939" y="619">Stakeholders</text>
    <text x="939" y="669">Budget</text>
  </g>

  <!-- Capacity detail lists -->
  <g class="detail-list">
    <text x="988" y="417">• Cold</text>
    <text x="988" y="438">• Warehouse</text>
    <text x="988" y="505">• Volunteers</text>
    <text x="988" y="524">• Expertise &amp;</text>
    <text x="999" y="542">Training</text>
    <text x="988" y="560">• Attitudes &amp;</text>
    <text x="999" y="578">Belief</text>
    <text x="988" y="596">• Collaboration</text>
    <text x="988" y="614">• Executive</text>
    <text x="999" y="632">Support</text>
  </g>
</svg>
</body>
</html>
```